New company looking for logo, for business cards and email signature.
we provide Safety, Training and Project Management Services to Mining and Transport sectors.

HALVORN CONSULTANCY, Tom Ashcrove, Principal Consultant, 0491362817, halvornconsultancy@postvale.example , Unit 412,KestwickRidge Business Hub,817 Tulloch Road, Mackay, 4832.
Sustainable Production through Safety, Training and Leadership.

```html
<!DOCTYPE html>
<html lang="en">
<head>
<meta charset="utf-8">
<title>Halvorn Consultancy – Business Card</title>
<link href="https://fonts.googleapis.com/css2?family=Cabin:wght@500&family=Questrial&family=Roboto+Condensed:wght@700&display=swap" rel="stylesheet">
<style>
  :root {
    --board: #b3b3b3;
    --card: #1b1b1b;
    --card-deep: #141414;
    --gold: #c9a43f;
    --label-gold: #e0b526;
    --text-light: #e6e6e6;
    --band: #ffffff;
    --band-text: #111111;
  }
  * { margin: 0; padding: 0; box-sizing: border-box; }
  html, body { width: 1200px; height: 1000px; overflow: hidden; background: var(--board); }
  .board { position: relative; width: 1200px; height: 1000px; }
  .card {
    position: absolute;
    background: linear-gradient(180deg, var(--card) 0%, var(--card-deep) 100%);
    overflow: hidden;
  }
  .card--hero { left: 20px; top: 20px; width: 1160px; height: 583px; }
  .card--front { left: 20px; top: 628px; width: 562px; height: 344px; }
  .card--back { left: 618px; top: 628px; width: 562px; height: 344px; }

  .brand { position: absolute; display: flex; align-items: center; }
  .brand__mark { border-radius: 50%; background: var(--gold); flex: none; }
  .brand__name {
    font-family: "Cabin", sans-serif;
    font-weight: 500;
    color: var(--gold);
    white-space: nowrap;
  }
  .card--hero .brand { left: 246px; top: 236px; }
  .card--hero .brand__mark { width: 92px; height: 92px; margin-right: 20px; }
  .card--hero .brand__name { font-size: 48px; letter-spacing: 0; }
  .card--front .brand { left: 56px; top: 33px; }
  .card--front .brand__mark { width: 62px; height: 62px; margin-right: 14px; }
  .card--front .brand__name { font-size: 31.5px; letter-spacing: 0; }

  .person {
    position: absolute; left: 125px; top: 226px; width: 312px;
    text-align: center; color: var(--text-light);
    font-family: "Questrial", sans-serif;
  }
  .person__name {
    font-size: 37px; font-variant: small-caps; letter-spacing: 0.5px;
    line-height: 42px; border-bottom: 1px solid var(--text-light);
  }
  .person__role { font-size: 19px; letter-spacing: 0.5px; margin-top: 4px; }

  .contact {
    position: absolute; left: 90px; top: 106px;
    font-family: "Questrial", sans-serif; color: var(--text-light); font-size: 19px; line-height: 24px;
  }
  .contact__row { display: flex; }
  .contact__label { color: var(--label-gold); width: 65px; }
  .contact__address { margin-top: 12px; line-height: 27px; }
  .contact__address span { display: block; }
  .contact__address span + span { padding-left: 39px; }

  .tagline {
    position: absolute; left: 0; top: 290px; width: 562px; height: 32px;
    background: var(--band); color: var(--band-text);
    font-family: "Roboto Condensed", sans-serif; font-weight: 700; font-size: 17px;
    display: flex; align-items: center; justify-content: center; letter-spacing: 0.2px;
    white-space: nowrap;
  }
</style>
</head>
<body>
<main class="board">
  <section class="card card--hero">
    <div class="brand">
      <span class="brand__mark"></span>
      <span class="brand__name">HALVORN CONSULTANCY</span>
    </div>
  </section>

  <section class="card card--front">
    <div class="brand">
      <span class="brand__mark"></span>
      <span class="brand__name">HALVORN CONSULTANCY</span>
    </div>
    <div class="person">
      <div class="person__name">Tom Ashcrove</div>
      <div class="person__role">PRINCIPAL CONSULTANT</div>
    </div>
  </section>

  <section class="card card--back">
    <div class="contact">
      <div class="contact__row"><span class="contact__label">Phone</span><span>: 0491362817</span></div>
      <div class="contact__row"><span class="contact__label">Email</span><span>: halvornconsultancy@postvale.example</span></div>
      <div class="contact__address">
        <span>Unit 412, KestwickRidge Business Hub,</span>
        <span>817 Tulloch Road, Mackay, 4832.</span>
      </div>
    </div>
    <div class="tagline">SUSTAINABLE PRODUCTION THROUGH SAFETY, TRAINING AND LEADERSHIP</div>
  </section>
</main>
</body>
</html>
```